Computer Company needs a Business card design

We need a business card design for our business. We assist people to transition to the QLX (Quorra Linkwave Exchange). The Australian Government-owned qlx™ network is a brand new telecommunications network currently being rolled out across Australia, giving access to a reliable broadband connection. Our niche market will predominantly be domestic customers in the 50+ age bracket. The assistance that we provide is everything from arranging the equipment, arranging the plan and contract term, appointment times, final testing of the network and any tweaks that need to be made. We basically PM the transition from start to finish. The business card design should be minimalist, should communicate loyalty and stability, should be easy to read and clearly explain what we do. We have asked for front and back. However, the back of the card does not have to include much information at all. It could be just a small design, or a repeat of our phone number. Up to you. The attached file only says what is required on the card. It does not specify where to arrange the text, what fonts to use, etc etc. As much as we would like to give you more info, due to our very limited design ability, we are not really able to send you any rough, or otherwise, designs of what we are after. Hopefully the above description is enough for you.

```html
<!DOCTYPE html>
<html lang="en">
<head>
<meta charset="utf-8">
<title>QLX Made Easy – Business Card</title>
<link href="https://fonts.googleapis.com/css2?family=Open+Sans:wght@400;600;700&display=swap" rel="stylesheet">
<style>
  :root {
    --backdrop: #d9d9d9;
    --card-dark: #050505;
    --card-light: #f4f4f4;
    --ink-dark: #1c1c1c;
    --ink-mid: #444444;
    --ink-light: #f2f2f2;
    --rule: #5a5a5a;
  }
  * { box-sizing: border-box; margin: 0; padding: 0; }
  html, body {
    width: 1200px; height: 904px; overflow: hidden;
    background: var(--backdrop);
    font-family: "Open Sans", Arial, sans-serif;
  }
  .sheet {
    position: relative; width: 1200px; height: 904px;
    display: flex; flex-direction: column; align-items: center; justify-content: center; gap: 40px;
  }
  .card {
    position: relative; width: 700px; height: 400px;
    box-shadow: 0 6px 18px rgba(0,0,0,0.25);
  }
  .card--back { background: var(--card-dark); display: flex; align-items: center; justify-content: center; }
  .card--front { background: var(--card-light); }

  .brand { display: flex; flex-direction: column; align-items: flex-start; }
  .brand__name {
    font-weight: 700; font-size: 56px; line-height: 1; letter-spacing: -1px;
  }
  .brand__tagline {
    font-weight: 700; font-size: 9.5px; letter-spacing: 0.4px; text-transform: uppercase; margin-top: 4px;
  }
  .card--back .brand__name, .card--back .brand__tagline { color: var(--ink-light); }
  .card--front .brand__name, .card--front .brand__tagline { color: var(--ink-dark); }

  .card--front .brand { position: absolute; left: 110px; top: 200px; }

  .divider {
    position: absolute; left: 400px; top: 95px; width: 2px; height: 120px; background: var(--rule);
  }
  .contact { position: absolute; left: 440px; top: 112px; color: var(--ink-mid); }
  .contact__name { font-weight: 700; font-size: 21px; color: var(--ink-dark); margin-bottom: 14px; }
  .contact__line { font-size: 17px; line-height: 1.5; }
</style>
</head>
<body>
  <main class="sheet">
    <section class="card card--back" aria-label="Card back">
      <div class="brand">
        <span class="brand__name">QLXME</span>
        <span class="brand__tagline">Quorra Linkwave Exchange - Made Easy</span>
      </div>
    </section>

    <section class="card card--front" aria-label="Card front">
      <div class="brand">
        <span class="brand__name">QLXME</span>
        <span class="brand__tagline">Quorra Linkwave Exchange - Made Easy</span>
      </div>
      <div class="divider"></div>
      <div class="contact">
        <p class="contact__name">Dale Hartwell</p>
        <p class="contact__line">0412508336</p>
        <p class="contact__line">www.qlxmadeeasy.com.au</p>
      </div>
    </section>
  </main>
</body>
</html>
```